Web site for Tree Removal Company

What we are looking for:
-------------------------------
Looking for a wordpress web site, you can provide your own template or we can supply you with one (http://pelorin.vextura.com).

What we do
---------------
To see what we do please go to google Australia and google "Tree removal Sydney" or "Tree Removal Melbourne".

Web site requirements
-----------------------------
We prefer you to use our template as it has all our requirements in already.
- Responsive.
- Based on Wordpress.
- Full complaint and compatible with plugs.

Look, Feel and Appearance
------------------------------------
Please use the logo (see attached), for colour scheme, look and feel of the web site.

Thank you for your time and effort!

Target Market(s)

Tree Removal for Residential Homes

Industry/Entity Type

It Company

Number of Pages Required

4 page

Font styles to use
Serif
Sans Serif

Requirements
Must have
• Wordpress
Nice to have
• Original artwork, images and text
Should not have
• non related images or wording

```html
<!DOCTYPE html>
<html lang="en">
<head>
<meta charset="utf-8">
<title>Arborline Tree Removal</title>
<link href="https://fonts.googleapis.com/css2?family=Open+Sans:wght@400;600;700&display=swap" rel="stylesheet">
<style>
:root{
  --black:#050505;
  --green:#5fc24a;
  --green-dark:#3f8f2f;
  --text:#555;
  --light:#efefef;
  --rule:#d9d9d9;
  --white:#fff;
}
*{box-sizing:border-box;margin:0;padding:0}
html,body{width:1200px;height:2916px;overflow:hidden;background:var(--white);font-family:"Open Sans",Arial,sans-serif;color:var(--text)}
.page{position:relative;width:1200px;height:2916px}

.site-header{height:70px;background:var(--black);display:flex;align-items:center;padding:0 80px 0 110px}
.brand{display:flex;align-items:center;gap:10px;color:var(--white);font-size:17px;font-weight:600}
.brand-mark{width:22px;height:22px;border-radius:50%;background:var(--green)}
.main-nav{margin-left:auto;display:flex;gap:26px;align-items:center}
.main-nav a{color:var(--white);text-decoration:none;font-size:14px;font-weight:600}
.search{margin-left:22px;width:150px;height:24px;background:var(--white);border-radius:3px;font-size:11px;color:#999;padding:4px 8px}

.hero{position:relative;height:620px;background:
  linear-gradient(180deg,#2c3a1f 0%,#4a6b2c 35%,#6a9a37 55%,#8fcc3e 75%,#a6dc48 100%)}
.hero-arrow{position:absolute;top:318px;width:44px;height:44px;border-radius:50%;background:rgba(0,0,0,.75);display:flex;align-items:center;justify-content:center}
.hero-arrow.prev{left:68px}.hero-arrow.next{right:68px}

.services{height:290px;background:var(--light);display:flex;justify-content:center;gap:86px;padding-top:30px}
.service{width:176px;text-align:center}
.service-icon{width:176px;height:176px;border-radius:50%;background:var(--black);display:flex;align-items:center;justify-content:center}
.service-title{margin-top:20px;color:var(--green);font-size:22px;font-weight:600}

.about{display:flex;gap:36px;padding:30px 80px 0;height:360px;overflow:hidden}
.about-photo{flex:0 0 520px;width:520px;height:300px;background:linear-gradient(135deg,#9fc86a,#6e8a4a 50%,#b9b9b0)}
.about-body h2{color:var(--green);font-size:28px;font-weight:700;margin:4px 0 14px}
.about-body p{font-size:13px;line-height:22px}
.read-more{display:block;margin-top:10px;color:var(--green);font-size:13px}

.divider{height:1px;background:var(--rule);margin:20px 80px 0}

.updates{display:flex;gap:48px;padding:30px 80px 0;height:460px;overflow:hidden}
.column{flex:1}
.column h3{color:var(--green);font-size:20px;font-weight:600;margin-bottom:12px}
.post{display:flex;gap:16px;margin-bottom:16px}
.post-thumb{flex:0 0 92px;height:104px;background:linear-gradient(160deg,#8fbc5a,#4d7330)}
.post-title{color:var(--green);font-size:10px;font-weight:700;text-transform:uppercase}
.post-date{font-size:9px;color:#999;margin:2px 0 6px}
.post p{font-size:11px;line-height:16px}
.post .read-more{font-size:10px;margin-top:2px}
.news-item{margin-bottom:12px}

.gallery{position:relative;height:770px;background:linear-gradient(180deg,#f4f4f4,#dcdcdc 50%,#f0f0f0);padding:120px 0 0 200px}
.gallery-grid{display:grid;grid-template-columns:repeat(3,200px);gap:84px 88px}
.tile{position:relative;width:200px;height:200px;border:6px solid #9a9a9a;background:linear-gradient(160deg,#a4c86b,#567a34)}
.tile-overlay{position:absolute;inset:0;background:rgba(0,0,0,.55);display:flex;flex-direction:column;align-items:center;justify-content:center;color:var(--white);font-size:16px;gap:8px}

.site-footer{height:289px;background:var(--black);display:flex;padding:36px 80px 0;color:var(--white);overflow:hidden}
.footer-col{flex:1}
.footer-col h4{font-size:26px;font-weight:400;margin-bottom:18px}
.footer-col li{list-style:none;font-size:12px;line-height:26px;color:#ddd}
.social{display:flex;align-items:center;gap:12px;font-size:12px;margin-bottom:16px}
.social span.dot{width:26px;height:26px;border-radius:50%;background:#3a3a3a}
.contact{display:flex;align-items:flex-start;gap:8px;font-size:12px;line-height:18px;margin-bottom:8px;color:#ddd}
.copyright{height:36px;background:#1a1a1a;color:#bbb;font-size:11px;text-align:center;line-height:36px}
</style>
</head>
<body>
<div class="page">
  <header class="site-header">
    <div class="brand"><span class="brand-mark"></span>Arborline</div>
    <nav class="main-nav">
      <a href="#">Home</a><a href="#">About</a><a href="#">Product</a><a href="#">Blog</a><a href="#">News</a><a href="#">Gallery</a><a href="#">Contact us</a>
      <div class="search">Search</div>
    </nav>
  </header>

  <section class="hero" role="img" aria-label="Avenue of tall trees over a bright green lawn">
    <span class="hero-arrow prev"><svg width="16" height="16" viewBox="0 0 16 16"><path d="M10 2 4 8l6 6" fill="none" stroke="#fff" stroke-width="2.5"/></svg></span>
    <span class="hero-arrow next"><svg width="16" height="16" viewBox="0 0 16 16"><path d="M6 2l6 6-6 6" fill="none" stroke="#fff" stroke-width="2.5"/></svg></span>
  </section>

  <section class="services">
    <div class="service"><div class="service-icon"><svg width="80" height="80" viewBox="0 0 80 80"><circle cx="40" cy="30" r="22" fill="#fff"/><rect x="36" y="45" width="8" height="28" fill="#fff"/></svg></div><div class="service-title">Lorem Ipsum</div></div>
    <div class="service"><div class="service-icon"><svg width="80" height="80" viewBox="0 0 80 80"><path d="M15 65C15 30 40 12 68 12 68 40 50 65 15 65Z" fill="#fff"/><path d="M15 65 58 22" stroke="#000" stroke-width="2"/></svg></div><div class="service-title">Lorem Ipsum</div></div>
    <div class="service"><div class="service-icon"><svg width="80" height="80" viewBox="0 0 80 80" stroke="#fff" stroke-width="4" fill="none"><path d="M40 72V10M40 30 24 18M40 30l16-12M40 48 22 36M40 48l18-12M40 62 26 54M40 62l14-8"/></svg></div><div class="service-title">Lorem Ipsum</div></div>
    <div class="service"><div class="service-icon"><svg width="80" height="80" viewBox="0 0 80 80"><circle cx="40" cy="22" r="10" fill="#fff"/><path d="M40 32v16" stroke="#fff" stroke-width="4"/><path d="M20 46h40l-6 26H26Z" fill="#fff"/></svg></div><div class="service-title">Lorem Ipsum</div></div>
  </section>

  <section class="about">
    <div class="about-photo" role="img" aria-label="Young tree staked with a support bracket"></div>
    <div class="about-body">
      <h2>Lorem Ipsum is simply</h2>
      <p>Our crews remove unsafe and unwanted trees from residential homes with care and skill. Every job starts with a site check, a clear quote and a plan to protect your house, fences and gardens. We fell, section and lower each limb, grind the stump below ground and take away all green waste, leaving the yard clean and tidy. Fully insured arborists work on every project, large or small, across the whole metro area and the surrounding suburbs.</p>
      <span class="read-more">read more</span>
    </div>
  </section>

  <div class="divider"></div>

  <section class="updates">
    <div class="column">
      <h3>Upcoming Blog</h3>
      <article class="post"><div class="post-thumb" role="img" aria-label="Tree trunk in a garden"></div><div><div class="post-title">Lorem ipsum is simply dummy text of the printing industry</div><div class="post-date">Posted on 12 June 2013</div><p>Tree services across the region with careful crews, safe removal, stump grinding and cleanup of every branch left behind on site.</p><span class="read-more">read more</span></div></article>
      <article class="post"><div class="post-thumb" role="img" aria-label="Garden hedge"></div><div><div class="post-title">Lorem ipsum is simply dummy text of the printing industry</div><div class="post-date">Posted on 18 June 2013</div><p>Tree services across the region with careful crews, safe removal, stump grinding and cleanup of every branch left behind on site.</p><span class="read-more">read more</span></div></article>
      <article class="post"><div class="post-thumb" role="img" aria-label="Staked sapling"></div><div><div class="post-title">Lorem ipsum is simply dummy text of the printing industry</div><div class="post-date">Posted on 24 June 2013</div><p>Tree services across the region with careful crews, safe removal, stump grinding and cleanup of every branch left behind on site.</p><span class="read-more">read more</span></div></article>
    </div>
    <div class="column">
      <h3>Ol News</h3>
      <article class="news-item post"><div><div class="post-title">Lorem ipsum is simply dummy text of the printing industry</div><div class="post-date">Posted on 02 July 2013</div><p>Tree services across the region with careful crews, safe removal, stump grinding and cleanup of every branch left behind on site.</p><span class="read-more">read more</span></div></article>
      <article class="news-item post"><div><div class="post-title">Lorem ipsum is simply dummy text of the printing industry</div><div class="post-date">Posted on 09 July 2013</div><p>Tree services across the region with careful crews, safe removal, stump grinding and cleanup of every branch left behind on site.</p><span class="read-more">read more</span></div></article>
      <article class="news-item post"><div><div class="post-title">Lorem ipsum is simply dummy text of the printing industry</div><div class="post-date">Posted on 16 July 2013</div><p>Tree services across the region with careful crews, safe removal, stump grinding and cleanup of every branch left behind on site.</p><span class="read-more">read more</span></div></article>
      <article class="news-item post"><div><div class="post-title">Lorem ipsum is simply dummy text of the printing industry</div><div class="post-date">Posted on 23 July 2013</div><p>Tree services across the region with careful crews, safe removal, stump grinding and cleanup of every branch left behind on site.</p><span class="read-more">read more</span></div></article>
    </div>
  </section>

  <section class="gallery" role="img" aria-label="Faint background of a tree-lined garden">
    <div class="gallery-grid">
      <div class="tile" role="img" aria-label="Tree in a park"><div class="tile-overlay"><svg width="30" height="30" viewBox="0 0 30 30" fill="none" stroke="#fff" stroke-width="3"><circle cx="12" cy="12" r="8"/><path d="M18 18l9 9"/></svg>Lorem Ipsum</div></div>
      <div class="tile" role="img" aria-label="Cleared stump on a lawn"></div>
      <div class="tile" role="img" aria-label="Green shrubs"></div>
      <div class="tile" role="img" aria-label="Large shade tree"></div>
      <div class="tile" role="img" aria-label="Row of trees by a road"></div>
      <div class="tile" role="img" aria-label="Trimmed tree with support"></div>
    </div>
  </section>

  <footer class="site-footer">
    <div class="footer-col"><h4>Navigation</h4><ul><li>Home</li><li>About us</li><li>Product</li><li>Blog</li><li>News</li><li>Gallery</li></ul></div>
    <div class="footer-col"><h4>For Members</h4><ul><li>Forums</li><li>Promotion</li><li>Sign in</li><li>News</li></ul></div>
    <div class="footer-col"><h4>Follow us</h4>
      <div class="social"><span class="dot"></span>Friendnet</div>
      <div class="social"><span class="dot"></span>Circleplus</div>
      <div class="social"><span class="dot"></span>Chirper</div>
    </div>
    <div class="footer-col"><h4>Our Location</h4>
      <div class="contact"><svg width="12" height="16" viewBox="0 0 12 16"><path d="M6 0a6 6 0 0 1 6 6c0 4-6 10-6 10S0 10 0 6a6 6 0 0 1 6-6Z" fill="#fff"/></svg>88 Ironbark Place,<br>Glenvale NSW 2150</div>
      <div class="contact"><svg width="14" height="14" viewBox="0 0 14 14"><path d="M3 0l3 3-2 2a8 8 0 0 0 5 5l2-2 3 3-2 3C6 14 0 8 0 3Z" fill="#fff"/></svg>+61 2 5550 0148</div>
      <div class="contact"><svg width="14" height="10" viewBox="0 0 14 10"><rect width="14" height="10" fill="#fff"/><path d="M0 0l7 5 7-5" fill="none" stroke="#000"/></svg>info@arborline.com</div>
    </div>
  </footer>
  <div class="copyright">Copyright © 2013 Arborline. All Rights Reserved.</div>
</div>
</body>
</html>
```